Business Cards For Glintwell
Desmond Kuvetti
Simple
CEO and Founder
2871 Pellfield Ln Brockville Ontario K3P2c8
Desmond@Kuvetti-mail.test
Keep it simple and clean. We want the logo BIG on the one side and company info on the other. If you can get some type of interlock going from bad to restored too that might look nice faded as a background on one of the sides.
750PineRidgeRnR 750PineRidgeRnR
https://www.socialpage.test/750PineRidgeRR/photos/pb.382915067214433.-1109384000.1285719304./517293048116520/?type=3&theater this is a good picture that would be nice to have one one side of the cards faded out
Logo has been uploaded.
Grafto Grafto
kindly upload logo

```html
<!DOCTYPE html>
<html lang="en">
<head>
<meta charset="utf-8">
<title>Glintwell Business Cards</title>
<link rel="stylesheet" href="https://fonts.googleapis.com/css2?family=Oswald:wght@600&family=Open+Sans:wght@400;700&display=swap">
<style>
  :root {
    --backdrop: #2b2b2c;
    --card: #fbfbfb;
    --card-shade: #ececec;
    --navy: #2d3a78;
    --navy-deep: #1f2a5e;
    --swoosh: #cfd2d8;
    --teal: #1fa3b0;
    --ink: #3b3b3b;
    --muted: #666;
  }
  * { box-sizing: border-box; margin: 0; padding: 0; }
  html, body {
    width: 1200px; height: 693px; overflow: hidden;
    background: var(--backdrop);
  }
  .stage { position: relative; width: 1200px; height: 693px; }
  .card {
    position: absolute;
    width: 497px; height: 283px;
    border-radius: 18px;
    background: linear-gradient(160deg, var(--card) 55%, var(--card-shade));
    overflow: hidden;
  }
  .card--front { left: 211px; top: 29px; }
  .card--back { left: 473px; top: 336px; }

  .front-band { position: absolute; left: 0; top: 0; width: 140px; height: 283px; }

  .wordmark {
    font-family: "Oswald", sans-serif;
    font-weight: 600;
    color: var(--navy);
    letter-spacing: 1px;
    line-height: 1;
  }
  .card--front .wordmark {
    position: absolute; left: 125px; top: 26px;
    font-size: 40px;
  }
  .card--back .wordmark {
    position: absolute; left: 0; right: 0; top: 108px;
    text-align: center; font-size: 56px;
  }

  .holder {
    position: absolute; left: 125px; top: 118px;
    font-family: "Open Sans", sans-serif;
  }
  .holder-name { font-size: 22px; font-weight: 700; color: var(--teal); line-height: 1.1; }
  .holder-role { font-size: 14px; color: var(--ink); margin-top: 3px; }

  .contacts {
    position: absolute; left: 125px; top: 184px;
    list-style: none;
    font-family: "Open Sans", sans-serif;
    font-size: 12.5px; color: var(--muted);
  }
  .contacts li { display: flex; align-items: center; height: 17px; }
  .contacts svg { width: 11px; height: 11px; margin-right: 9px; flex: none; }
</style>
</head>
<body>
<div class="stage">

  <section class="card card--front" aria-label="Card front">
    <svg class="front-band" viewBox="0 0 140 283" aria-hidden="true">
      <path d="M0 0 H118 C70 55 62 170 128 283 H0 Z" fill="var(--swoosh)"/>
      <path d="M0 0 H100 C52 60 48 175 112 283 H0 Z" fill="var(--navy)"/>
    </svg>

    <div class="wordmark">GLINTWELL</div>

    <div class="holder">
      <div class="holder-name">Desmond Kuvetti</div>
      <div class="holder-role">Founder</div>
    </div>

    <ul class="contacts">
      <li>
        <svg viewBox="0 0 12 12"><path d="M2.5 1 L4.5 1 L5.3 3.5 L4 4.5 C4.6 6 6 7.4 7.5 8 L8.5 6.7 L11 7.5 L11 9.5 C11 10.3 10.3 11 9.5 11 C5 11 1 7 1 2.5 C1 1.7 1.7 1 2.5 1 Z" fill="var(--teal)"/></svg>
        012 345 6789
      </li>
      <li>
        <svg viewBox="0 0 12 12"><rect x="1" y="2.5" width="10" height="7" rx="1" fill="var(--teal)"/><path d="M1.5 3 L6 6.5 L10.5 3" stroke="#fff" stroke-width="1" fill="none"/></svg>
        name@mail.test
      </li>
      <li>
        <svg viewBox="0 0 12 12"><circle cx="6" cy="6" r="5" fill="var(--teal)"/><path d="M1 6 H11 M6 1 C3.5 4 3.5 8 6 11 M6 1 C8.5 4 8.5 8 6 11" stroke="#fff" stroke-width="0.8" fill="none"/></svg>
        www.yoursite.test
      </li>
      <li>
        <svg viewBox="0 0 12 12"><circle cx="6" cy="6" r="5" fill="var(--teal)"/></svg>
        @yourhandle
      </li>
    </ul>
  </section>

  <section class="card card--back" aria-label="Card back">
    <div class="wordmark">GLINTWELL</div>
  </section>

</div>
</body>
</html>
```